Business Card for By Karel Voss

Looking to have a business card designed for my lifestyle and fitness company. My company offers personal training, online programming and nutrition advice based out of London, United Kingdom.

I'd like to see modern, sleek designs, focusing on black, matte black or matte grey. Design doesn't need to be overly descriptive as this will also be used as a personal business card. I've included my logo.

Please note that my company is no longer called "By Karel Voss" but instead "By Karel Voss", this is because of my other ventures. Therefore please don't use the "fitness by karel voss" text.

information about my company can be found at www.bykarelvoss.com

Company is also based out of London (United Kingdom) & Sydney (Australia) this could be reflected on the card.

Industry/Entity Type

Business

Contact Information for Business Card

Karel Voss
+44 7382 615027
karel@bykarelvoss.com
www.bykarelvoss.com

Font styles to use
Sans Serif

Requirements
Must have
• All contact details and inclusion of my logo.

```html
<!DOCTYPE html>
<html lang="en">
<head>
<meta charset="utf-8">
<title>Business Cards – By Karel Voss</title>
<link rel="stylesheet" href="https://fonts.googleapis.com/css2?family=Roboto+Condensed:wght@400;700&display=swap">
<style>
  :root {
    --backdrop: #000000;
    --card: #161616;
    --silver: #cfcfcf;
    --silver-dim: #a9a9a9;
    --rule: #d8d8d8;
    --text-font: "Roboto Condensed", Arial, sans-serif;
  }
  * { box-sizing: border-box; margin: 0; padding: 0; }
  html, body { width: 1200px; height: 1200px; overflow: hidden; background: var(--backdrop); }
  body { position: relative; font-family: var(--text-font); color: var(--silver); }

  .card {
    position: absolute;
    width: 920px;
    height: 520px;
    background: var(--card);
  }
  .card--front { left: 80px; top: 50px; }
  .card--back  { left: 200px; top: 640px; }

  .rule { position: absolute; height: 3px; background: var(--rule); }

  .brand { position: absolute; display: flex; flex-direction: column; align-items: center; }
  .brand__mark {
    width: 110px; height: 110px; border-radius: 50%;
    background: var(--silver);
    margin-bottom: 40px;
  }
  .brand__name {
    font-family: var(--text-font);
    font-weight: 700;
    font-size: 40px;
    letter-spacing: 1px;
    text-transform: uppercase;
    color: var(--silver);
    white-space: nowrap;
    line-height: 1;
  }

  /* front */
  .card--front .brand { left: 0; right: 0; top: 105px; }
  .card--front .rule--left  { left: 30px;  width: 270px; top: 273px; }
  .card--front .rule--right { left: 620px; width: 270px; top: 273px; }

  /* back */
  .card--back .brand { left: 70px; width: 340px; top: 95px; }
  .card--back .brand__mark { width: 100px; height: 100px; }
  .card--back .brand__name { font-size: 36px; }
  .card--back .rule--left  { left: 0;     width: 40px;  top: 251px; }
  .card--back .rule--mid   { left: 460px; width: 390px; top: 251px; }
  .card--back .rule--right { left: 866px; width: 54px;  top: 251px; }

  .holder { position: absolute; right: 70px; top: 150px; text-align: right; }
  .holder__name { font-size: 48px; font-weight: 400; color: #f0f0f0; line-height: 1; }
  .holder__role { font-size: 22px; color: var(--silver-dim); margin-top: 8px; }

  .contacts { position: absolute; right: 50px; top: 295px; list-style: none; }
  .contacts__item {
    display: flex; align-items: center; justify-content: flex-end;
    gap: 16px; font-size: 24px; color: var(--silver); height: 50px;
  }
  .contacts__icon { width: 24px; height: 24px; flex: none; }
</style>
</head>
<body>

  <section class="card card--front" aria-label="Business card front">
    <div class="brand">
      <div class="brand__mark"></div>
      <div class="brand__name">By Karel Voss</div>
    </div>
    <div class="rule rule--left"></div>
    <div class="rule rule--right"></div>
  </section>

  <section class="card card--back" aria-label="Business card back">
    <div class="brand">
      <div class="brand__mark"></div>
      <div class="brand__name">By Karel Voss</div>
    </div>
    <div class="rule rule--left"></div>
    <div class="rule rule--mid"></div>
    <div class="rule rule--right"></div>

    <div class="holder">
      <div class="holder__name">Karel Voss</div>
      <div class="holder__role">Director</div>
    </div>

    <ul class="contacts">
      <li class="contacts__item">+44 7382 615027
        <svg class="contacts__icon" viewBox="0 0 24 24" fill="none" stroke="currentColor" stroke-width="1.6">
          <rect x="2" y="2" width="20" height="20" rx="3"/>
          <path d="M8 6l2 3-1.5 1.5c.8 2 2.5 3.7 4.5 4.5L14.5 13.5l3 2-1 2.5c-5 0-10-5-10-10z"/>
        </svg>
      </li>
      <li class="contacts__item">karel@bykarelvoss.com
        <svg class="contacts__icon" viewBox="0 0 24 24" fill="none" stroke="currentColor" stroke-width="1.6">
          <rect x="2" y="5" width="20" height="14"/>
          <path d="M2 5l10 8 10-8"/>
        </svg>
      </li>
      <li class="contacts__item">www.bykarelvoss.com
        <svg class="contacts__icon" viewBox="0 0 24 24" fill="none" stroke="currentColor" stroke-width="1.6">
          <circle cx="12" cy="12" r="10"/>
          <ellipse cx="12" cy="12" rx="4.5" ry="10"/>
          <path d="M2 12h20M4 7h16M4 17h16"/>
        </svg>
      </li>
    </ul>
  </section>

</body>
</html>
```